Bright Harbour - website for leadership service

I would like help to use a Squarespace template for a simple website.
We already have a logo which will influence the colour choice and tone.
Clean lines for executive audience. it is an exclusive service. I have all the content ready to go.
Would like some images included.

I will upload the content soon.

Does NOT need SEO as it will be direct mailed. Also does NOT need to consider having any payment pages or enquiry form.
Thanks

Target Market(s)

Women executives - senior leaders. Stylish, serious and capable.

Coding

Coded - Design and coding required

Number of Pages Required

3 page

Colors
3176b5
fee18a

Requirements
Must have
• Sqaurespace template. And scrolling down page format.

To suit style of the blue and gold logo.
Nice to have
• Simple, Stylish and exclusive feel. Inspiring but not "New Age"
Should not have
• Too many colours.

No

```html
<!DOCTYPE html>
<html lang="en">
<head>
<meta charset="utf-8">
<title>Bright Harbour — Leadership for a New Era</title>
<link href="https://fonts.googleapis.com/css2?family=Jost:ital,wght@0,400;0,500;1,400&family=Montserrat:ital,wght@0,400;0,500;1,500&display=swap" rel="stylesheet">
<style>
:root{
  --blue:#3176b5;
  --gold:#fee18a;
  --gold-deep:#f6c85a;
  --ink:#111111;
  --grey:#5a5a5a;
  --white:#ffffff;
}
*{box-sizing:border-box;margin:0;padding:0}
html,body{width:1200px;height:4140px;overflow:hidden;background:var(--white)}
body{position:relative;font-family:"Jost",sans-serif;color:var(--ink)}
.abs{position:absolute}
section,header,footer{position:absolute;left:0;width:1200px}

/* header */
.site-header{top:0;height:114px;background:var(--white)}
.brand{position:absolute;display:flex;align-items:center;gap:10px;font-family:"Jost",sans-serif;font-size:17px;font-weight:500;color:#2a2a2a;white-space:nowrap}
.brand-dot{width:14px;height:14px;border-radius:50%;background:var(--gold-deep);display:block}
.nav{position:absolute;top:50px;left:472px;display:flex;gap:26px;align-items:center;font-size:16px;letter-spacing:1px}
.nav a{color:var(--ink);text-decoration:none}
.nav .current{color:#d8a93e;padding:4px 14px;border-radius:18px;box-shadow:0 0 10px rgba(246,200,90,.45)}
.social{position:absolute;display:flex;gap:16px}
.social span{width:11px;height:11px;border-radius:50%;background:var(--ink);display:block}

/* hero */
.hero{top:114px;height:574px}
.hero-photo{position:absolute;inset:0;background:linear-gradient(100deg,#8d8172 0%,#5c5247 30%,#4a3f36 60%,#2e2721 100%)}
.hero-title{position:absolute;right:112px;top:170px;text-align:right;color:var(--white)}
.hero-title h1{font-weight:500;font-size:58px;letter-spacing:-1px;line-height:1}
.hero-title p{font-size:40px;margin-top:10px;line-height:1}
.btn-gold{position:absolute;background:var(--gold);color:var(--ink);font-size:19px;display:flex;align-items:center;justify-content:center}

/* intro band */
.intro{top:688px;height:340px;background:var(--gold);text-align:center}
.intro .rule{position:absolute;left:563px;top:45px;width:74px;height:2px;background:var(--ink)}
.intro p{position:absolute;left:110px;width:980px;font-size:19px;line-height:29px}
.btn-outline{position:absolute;left:538px;top:242px;width:123px;height:56px;border:2px solid var(--ink);font-size:19px;display:flex;align-items:center;justify-content:center}

/* split sections */
.split{height:652px}
.photo{position:absolute}
.split h2{position:absolute;font-weight:500;font-size:34px}
.split h2 em{font-style:normal;color:var(--blue)}
.body{position:absolute;font-family:"Montserrat",sans-serif;font-size:13.5px;line-height:26px;color:var(--grey)}
.link{position:absolute;font-size:19px;text-decoration:underline;text-underline-offset:4px}

/* testimonial */
.testimonial{top:1680px;height:555px}
.testimonial-photo{position:absolute;inset:0;background:linear-gradient(180deg,#3a4650 0%,#25323d 45%,#1b2733 100%)}
.avatar{position:absolute;left:540px;top:100px;width:120px;height:120px;border-radius:50%;background:#c9b59c;border:3px solid var(--gold-deep)}
.t-name{position:absolute;left:0;width:1200px;top:245px;text-align:center;color:var(--gold-deep);font-size:42px}
.t-role{position:absolute;left:0;width:1200px;top:305px;text-align:center;color:var(--gold-deep);font-size:21px}
.t-quote{position:absolute;left:150px;width:900px;top:350px;text-align:center;color:var(--white);font-family:"Montserrat",sans-serif;font-size:14px;line-height:29px}
.quote-mark{position:absolute;color:var(--gold);font-family:"Jost",sans-serif;font-size:150px;line-height:1;font-weight:500}

/* checklist */
.checks{position:absolute;left:565px;top:2525px;width:530px;list-style:none;font-family:"Montserrat",sans-serif;font-size:13px;line-height:22px;color:var(--grey)}
.checks li{position:relative;padding-left:26px;margin-bottom:12px}
.checks svg{position:absolute;left:2px;top:4px}

/* resources */
.resources{top:2893px;height:569px;background:var(--blue)}
.resources h2{position:absolute;left:0;width:1200px;top:65px;text-align:center;color:var(--white);font-weight:500;font-size:33px}
.card{position:absolute;top:149px;width:312px}
.card-photo{height:220px}
.card h3{color:var(--white);font-weight:400;font-size:26px;margin-top:18px}
.card p{color:#e6eef7;font-family:"Montserrat",sans-serif;font-size:12.5px;line-height:22px;margin-top:8px;text-align:justify}

/* newsletter */
.newsletter{top:3462px;height:431px}
.newsletter-photo{position:absolute;inset:0;background:linear-gradient(160deg,#5c4a86 0%,#6a4f7e 40%,#4e3d5a 75%,#3b3040 100%)}
.newsletter h2{position:absolute;left:0;width:1200px;top:120px;text-align:center;color:var(--white);font-weight:500;font-size:34px}
.newsletter p{position:absolute;left:0;width:1200px;top:176px;text-align:center;color:var(--white);font-size:19px}
.field{position:absolute;left:279px;top:242px;width:488px;height:60px;border:2px solid var(--white);color:var(--white);font-size:19px;padding-left:14px;display:flex;align-items:center}

/* footer */
.site-footer{top:3893px;height:247px}
.f-text{position:absolute;font-size:16px;line-height:30px}
.f-rule{position:absolute;left:111px;top:169px;width:977px;height:1px;background:#cfcfcf}
.copyright{position:absolute;left:0;width:1200px;top:200px;text-align:center;font-size:16px}
</style>
</head>
<body>

<header class="site-header">
  <div class="brand" style="left:110px;top:48px"><span class="brand-dot"></span>Bright Harbour</div>
  <nav class="nav">
    <a class="current">HOME</a><a>ABOUT</a><a>TESTIMONIALS</a><a>RESOURCES</a><a>CONTACT</a>
  </nav>
  <div class="social" style="left:1042px;top:56px"><span></span><span></span></div>
</header>

<section class="hero">
  <div class="hero-photo" role="img" aria-label="Photo of a woman speaking into a microphone at a business audience"></div>
  <div class="hero-title">
    <h1>BRIGHT HARBOUR</h1>
    <p>New Era Of Business</p>
  </div>
  <div class="btn-gold" style="left:963px;top:316px;width:124px;height:57px">Read More</div>
</section>

<section class="intro">
  <div class="rule"></div>
  <p style="top:72px">BRIGHT HARBOUR is a premier leadership coaching service entirely focused on supporting women in executive roles to lead commercially successful businesses in ways that align with their core values and principles.</p>
  <p style="top:145px;font-style:italic">A new era of values-driven business has begun, led by women like you: capable, proven leaders who are challenging the status quo and redefining the meaning of business success.</p>
  <div class="btn-outline">Read More</div>
</section>

<section class="split" style="top:1028px">
  <h2 style="left:112px;width:510px;top:124px;text-align:center">What is <em>BRIGHT HARBOUR?</em></h2>
  <div class="body" style="left:112px;width:510px;top:188px;text-align:center">
    <p>Women are at the forefront of a global movement of leaders pioneering new business models. BRIGHT HARBOUR will connect you to this movement and get you excited about business leadership again.</p>
    <p style="margin-top:12px">What made business successful in the past is not working. Long established traditions of politicking, closed door decision making and a constant focus on short-term quick wins and shareholder profit are no longer a guarantee of good business results.</p>
    <p style="margin-top:12px;color:var(--blue);font-style:italic;font-weight:500">To be successful, businesses must deliver as much value for employees, customers, suppliers and wider communities, as they do for shareholders.</p>
  </div>
  <div class="link" style="left:319px;top:490px">Read More</div>
  <div class="photo" style="left:681px;top:80px;width:407px;height:485px;background:linear-gradient(170deg,#c8b8a6,#8a7461 50%,#4f4237)" role="img" aria-label="Photo of an audience seated at a business conference"></div>
</section>

<section class="testimonial">
  <div class="testimonial-photo" role="img" aria-label="Photo of a packed conference hall with speakers on stage"></div>
  <div class="avatar" role="img" aria-label="Portrait of the client"></div>
  <div class="t-name">Maren Calloway</div>
  <div class="t-role">CEO at Westbrook Trust</div>
  <div class="quote-mark" style="left:152px;top:260px">“</div>
  <div class="quote-mark" style="left:978px;top:260px">”</div>
  <p class="t-quote">I have had the pleasure of spending the last year working with Elise. Her measured guidance has been a pillar for my success this year. She helped me to find my voice and gave me the confidence to speak up where needed. Elise has helped me to prioritise my time to become more of a leader and less of an administrator. I feel so much more confident in my role with a clear vision into the future.</p>
  <svg class="abs" style="left:44px;top:255px" width="28" height="50" viewBox="0 0 28 50"><path d="M25 3 L4 25 L25 47" fill="none" stroke="#fff" stroke-width="2.5"/></svg>
  <svg class="abs" style="left:1136px;top:255px" width="28" height="50" viewBox="0 0 28 50"><path d="M3 3 L24 25 L3 47" fill="none" stroke="#fff" stroke-width="2.5"/></svg>
</section>

<section class="split" style="top:2235px">
  <div class="photo" style="left:111px;top:78px;width:408px;height:485px;background:linear-gradient(160deg,#d9d2c8,#a99886 50%,#5b4c40)" role="img" aria-label="Photo of a man presenting to a seated audience"></div>
  <h2 style="left:565px;top:113px">How will <em>BRIGHT HARBOUR help me?</em></h2>
  <div class="body" style="left:565px;width:520px;top:175px">No one understands as well as you, the blocks and challenges of working in current business models. BRIGHT HARBOUR will strengthen your leadership with new thinking, new models and the ability to tap into your own deep wisdom.</div>
  <div class="link" style="left:592px;top:497px">Read More</div>
</section>
<ul class="checks">
  <li><svg width="14" height="12" viewBox="0 0 14 12"><path d="M1 6 L5 10 L13 1" fill="none" stroke="#3176b5" stroke-width="2.5"/></svg>Navigate current business challenges without compromising your values.</li>
  <li><svg width="14" height="12" viewBox="0 0 14 12"><path d="M1 6 L5 10 L13 1" fill="none" stroke="#3176b5" stroke-width="2.5"/></svg>Find ways to deliver hard commercial imperatives with grace and ethical integrity.</li>
  <li><svg width="14" height="12" viewBox="0 0 14 12"><path d="M1 6 L5 10 L13 1" fill="none" stroke="#3176b5" stroke-width="2.5"/></svg>Get extra support to effectively challenge outdated ways of thinking and influence better ways of leading.</li>
  <li><svg width="14" height="12" viewBox="0 0 14 12"><path d="M1 6 L5 10 L13 1" fill="none" stroke="#3176b5" stroke-width="2.5"/></svg>Clean up negative patterns and habits in a high-trust setting. This is a deep process and one that needs an experienced guide.</li>
</ul>

<section class="resources">
  <h2>Related Resources</h2>
  <article class="card" style="left:111px">
    <div class="card-photo" style="background:linear-gradient(160deg,#e6e2dc,#b7aa9c 55%,#6e6258)" role="img" aria-label="Photo of a smiling woman at a roundtable workshop"></div>
    <h3>Leaders Forum 2019</h3>
    <p>Leaders Forum today announced the release of a new charter on the role of a modern company in society...</p>
  </article>
  <article class="card" style="left:444px">
    <div class="card-photo" style="background:linear-gradient(160deg,#c9c4bf,#7b7a7e 55%,#3a3d45)" role="img" aria-label="Photo of an audience applauding at an event"></div>
    <h3>Celia Marchetti</h3>
    <p>"Why are we spending untold energy trying to work our way up the ladder of a broken system? Instead of dreaming...</p>
  </article>
  <article class="card" style="left:776px">
    <div class="card-photo" style="background:linear-gradient(160deg,#e8e9ec,#9aa0ab 55%,#3b4250)" role="img" aria-label="Photo of a speaker addressing a seminar room"></div>
    <h3>Nora Whitfield | CEO</h3>
    <p>"Women are redefining leadership into something that is values-based, shifting the way power is expressed...</p>
  </article>
</section>

<section class="newsletter">
  <div class="newsletter-photo" role="img" aria-label="Blurred photo of a conference audience"></div>
  <h2>Subscribe to Our Newsletter</h2>
  <p>Sign up to receive news and updates.</p>
  <div class="field">Email Address</div>
  <div class="btn-gold" style="left:786px;top:242px;width:135px;height:60px">Sign Up</div>
</section>

<footer class="site-footer">
  <div class="brand" style="left:114px;top:84px"><span class="brand-dot"></span>Bright Harbour</div>
  <div class="f-text" style="left:415px;top:63px">48 Quayside Lane<br>Harbour City, NY 10020</div>
  <div class="f-text" style="left:726px;top:63px">hello@brightharbour.co<br>(555) 010-2040</div>
  <div class="social" style="left:1045px;top:94px"><span></span><span></span></div>
  <div class="f-rule"></div>
  <div class="copyright">Copyrights @ 2020 Bright Harbour. All Rights Reserved.</div>
</footer>

</body>
</html>
```